Comparison Website Design for Glue Website

Note: We don't have a logo, it's not needed. Just put placeholder.

We would like a website comparing A to B, simple elegant design, simplistic styling. Website is for helping people find the best glue to glue 2 things together. For example, Metal to wood, Metal to rubber, glass to fabric and so on. Select 2 options and be shown the best glue/adhesive for the job.

Purpose of the website:
Allowing someone to pick 2 materials they want to glue together, and showing them the best product for it. We want someone to select 2 materials like "Metal and Rubber". It'll then show the best glues/adhesives from best #1 to #5-10 other ones. The design is simple and doesn't need much detail.

Design rules:
Please design using bootstrap 4 with a modified 1440px width.

We're looking for 4 main pages:
Home Page, Compare Page, Category Page, Product Page.

Target Market(s)

Everyone

Industry/Entity Type

Adhesive

Number of Pages Required

3 page

Font styles to use
Sans Serif

Colors
876aae
b7a5cd
6b449b
e4daeb
fefeff

Requirements
Must have
• We like the following features of these designs:
https://pixelvane.example/shots/6401517-CoverLoom-Dashboard - Main menu with the drop down, this will change depending on the active page. If they are on a metal page they could be shown "glue metal to ___" options. We also like the simple table view in this design under "users" heading.

https://pixelvane.example/shots/6300662-Volt-Sketch-Quotation-Page - The entire colour palette is great! The simplicity of the design is great.

https://pixelvane.example/shots/8593973-Loans-Comparison-UI - The boxes at the top look great, if there was 2 of these with a compare icon between them and above that saying "glue metal to rubber" and it shows an icon/image or metal and glue... The table of products is also good, it has dot points and details which we like.

https://pixelvane.example/shots/4586351-Transfer-Money/attachments/4586351-Transfer-Money?mode=media - The right it shows which 2 products are selected (metal and rubber) for example, on the left it would say "best glue for metal and rubber". This is too detailed though, so it would need to be simplified nicely.

https://linquora.example/ - They do a good job of "comparing" 2 things and displaying integrations well. You can get lots of ideas from them linking A to B similar to what we want to show.

https://www.campaignflowreview.example/leadnest-vs-drivemint/ - This shows a good example of the hero section how it should look.

Features of each page to help you design:
Home Page-
Menu (shown in examples above)
Hero section (colour section) with a centre heading saying "what do you want to glue together" with 2 boxes below to select materials from.
List of most popular searches (metal to rubber, glass to wood, fabric to leather... repeat these to fill space).
List of popular products with basic details about each one (grid format, not list).
FAQs - You choose design for this
Content section (simple design, headings, paragraphs, dotpoints, images...)
Blog section - Simple 3 column grid with an image on top, heading, paragraph, button.

Compare Page-
Showing 2 materials in the colour hero section under or to the right of the heading and paragraph.
Best product (highlighted)
9 other products (list table)
3 column section saying glue (product a to ___) with other product that isn't product b + reverse of this.
Content section

Category page-
heading and breadcrumbs in hero section
Standard product list 1 column on the left with filters, 3 products shown on the right in grid format with basic details on each one.

Product page-
Image left, details on the right.
Keep the image smaller not 50% as we want it to not take up too much space vertically.
Under this put a table where this product ranks for gluing things together. for example #3 for gluing metal to rubber, #1 for glass to wood.
Content section.

Please note, keep this design flat, simple and pretty. We don't need it over-designed or detailed, we simply want a simple functionality website that clearly shows what we're looking for.

```html
<!DOCTYPE html>
<html lang="en">
<head>
<meta charset="utf-8">
<title>Glue Finder – Home</title>
<link href="https://fonts.googleapis.com/css2?family=Nunito+Sans:wght@400;600;700;800&display=swap" rel="stylesheet">
<style>
:root{
  --purple-dark:#6b449b;
  --purple:#876aae;
  --purple-light:#b7a5cd;
  --lilac:#e4daeb;
  --white:#fefeff;
  --ink:#1d1a22;
  --footer:#2f2147;
  --field:#f3f3f3;
  --rule:#d9d9d9;
}
*{box-sizing:border-box;margin:0;padding:0}
html,body{width:1200px;height:4158px;overflow:hidden}
body{position:relative;font-family:"Nunito Sans",Arial,sans-serif;color:var(--ink);background:var(--white)}
.abs{position:absolute}
.band-hero{left:0;top:0;width:1200px;height:1753px;background:linear-gradient(180deg,#6c45a0 0%,#7d5bab 100%)}
.band-content{left:0;top:2603px;width:1200px;height:1497px;background:linear-gradient(180deg,#987bbe 0%,#b7a5cd 100%)}
/* nav */
.logo-dot{left:124px;top:32px;width:58px;height:58px;border-radius:50%;background:var(--purple-light)}
.logo-name{left:192px;top:50px;font-size:16px;color:var(--lilac)}
.nav-link{top:53px;font-size:13px;color:var(--white)}
.nav-link.active{font-weight:700}
.nav-link.active::after{content:"";position:absolute;left:50%;top:22px;width:5px;height:5px;margin-left:-2.5px;border-radius:50%;background:var(--white)}
.nav-divider{left:987px;top:44px;width:1px;height:32px;background:var(--white);opacity:.8}
.nav-select{left:996px;top:46px;text-align:right;width:80px;color:var(--white);line-height:12px}
.nav-select small{display:block;font-size:9px;opacity:.85}
.nav-select b{font-size:9px;letter-spacing:.5px}
/* finder */
.card{background:var(--white);border-radius:3px;box-shadow:0 2px 6px rgba(0,0,0,.12)}
.finder{left:124px;top:148px;width:952px;height:349px}
.finder h1{position:absolute;top:55px;width:100%;text-align:center;font-size:25px;font-weight:600}
.select{position:absolute;top:139px;width:301px;height:47px;border:1px solid #cfcfcf;border-radius:2px;font-size:13px;text-align:center;line-height:45px;letter-spacing:.5px}
.select::after{content:"";position:absolute;right:18px;top:20px;border:5px solid transparent;border-top:5px solid #333}
.link-dots{position:absolute;left:452px;top:153px}
.btn{position:absolute;background:var(--purple-dark);color:var(--white);border-radius:30px;text-align:center;font-weight:700;letter-spacing:.6px}
.finder .btn{left:361px;top:237px;width:230px;height:57px;line-height:57px;font-size:14px}
.section-title{left:124px;font-size:20px;font-weight:700;color:var(--white);letter-spacing:1.5px}
.searches{left:124px;top:624px;width:952px;height:66px}
.search-pair{position:absolute;top:24px;font-size:13px;letter-spacing:.4px;display:flex;align-items:center;gap:8px}
/* products */
.product{width:302px;height:405px}
.product-shot{position:absolute;left:115px;top:33px;width:72px;height:125px;background:linear-gradient(180deg,#f1d800 0%,#d81f26 45%,#b1161c 100%)}
.product h3{position:absolute;left:25px;top:180px;width:260px;font-size:13.5px;font-weight:700;line-height:18px}
.product p{position:absolute;left:25px;top:224px;width:262px;font-size:11px;line-height:16px}
.view-more{position:absolute;right:25px;top:286px;font-size:10px;font-weight:700;text-decoration:underline}
.product .btn{left:24px;top:321px;width:254px;height:44px;line-height:44px;font-size:14px}
/* faq */
.faq-title{left:0;width:1200px;top:1820px;text-align:center;font-size:40px;font-weight:700}
.faq-sub{left:0;width:1200px;text-align:center;font-size:13px;font-weight:600}
.faq-list{left:284px;top:1990px;width:629px;border-top:1px solid var(--rule)}
.faq-item{height:54px;border-bottom:1px solid var(--rule);position:relative;font-size:13px;font-weight:700;line-height:54px}
.faq-item::after{content:"";position:absolute;right:4px;top:25px;border:4px solid transparent;border-top:4px solid #222}
.question-box{left:287px;top:2326px;width:626px;height:118px;background:var(--field);border-radius:2px;padding:24px 25px;font-size:11px;color:#555}
.submit{left:485px;top:2479px;width:230px;height:57px;line-height:57px;font-size:14px}
/* content */
.content-title{left:0;width:1200px;top:2668px;text-align:center;font-size:42px;font-weight:700}
.article{left:124px;top:2758px;width:952px;height:555px;overflow:hidden}
.article-photo{height:332px;background:linear-gradient(100deg,#f4f4f4 0%,#eceff2 35%,#aeb8c4 55%,#d8dbe0 70%,#ecd64a 90%,#e9d23c 100%)}
.article h2{position:absolute;left:81px;top:366px;font-size:21px;font-weight:700}
.article p{position:absolute;left:81px;top:410px;width:790px;font-size:13px;line-height:18px;color:#333}
/* blog */
.blog-title{left:0;width:1200px;top:3380px;text-align:center;font-size:40px;font-weight:700}
.post{top:3486px;width:302px;height:405px}
.post-photo{height:150px;background:linear-gradient(135deg,#3c3a1c 0%,#7f9a3a 40%,#9bc24a 60%,#c7d7d0 85%)}
.post h3{position:absolute;left:24px;top:182px;font-size:13.5px;font-weight:700}
.post p{position:absolute;left:24px;top:218px;width:256px;font-size:11px;line-height:16px}
.post .btn{left:24px;top:321px;width:254px;height:43px;line-height:43px;font-size:14px}
.all-posts{left:461px;top:3958px;width:278px;height:57px;line-height:57px;font-size:14px}
/* footer */
.footer{left:0;top:4100px;width:1200px;height:58px;background:var(--footer);color:var(--white);font-size:10px}
.footer-brand{position:absolute;left:124px;top:22px}
.footer-links{position:absolute;right:124px;top:20px}
.footer-links span{margin:0 6px}
</style>
</head>
<body>
<div class="abs band-hero"></div>
<div class="abs band-content"></div>

<header>
  <div class="abs logo-dot"></div>
  <div class="abs logo-name">Logo Placeholder</div>
  <nav>
    <span class="abs nav-link active" style="left:650px">Home</span>
    <span class="abs nav-link" style="left:725px">Compare</span>
    <span class="abs nav-link" style="left:821px">Category</span>
    <span class="abs nav-link" style="left:919px">Product</span>
    <span class="abs nav-divider"></span>
    <div class="abs nav-select"><small>Material to glue</small><b>SELECT ▾</b></div>
  </nav>
</header>

<section class="abs card finder">
  <h1>What do you want to glue together</h1>
  <div class="select" style="left:81px">METAL</div>
  <svg class="link-dots" width="50" height="12" viewBox="0 0 50 12"><circle cx="6" cy="6" r="5" fill="#b7a5cd"/><circle cx="25" cy="6" r="5" fill="#b7a5cd"/><circle cx="44" cy="6" r="5" fill="#b7a5cd"/></svg>
  <div class="select" style="left:570px">RUBBER</div>
  <div class="btn">Find Adhesive</div>
</section>

<h2 class="abs section-title" style="top:562px">POPULAR SEARCHES</h2>
<section class="abs card searches">
  <div class="search-pair" style="left:42px">METAL <svg width="32" height="8"><line x1="2" y1="4" x2="30" y2="4" stroke="#6b449b" stroke-width="2"/><circle cx="8" cy="4" r="3" fill="#6b449b"/><circle cx="16" cy="4" r="3" fill="#6b449b"/><circle cx="24" cy="4" r="3" fill="#6b449b"/></svg> RUBBER</div>
  <div class="search-pair" style="left:284px">GLASS <svg width="32" height="8"><line x1="2" y1="4" x2="30" y2="4" stroke="#6b449b" stroke-width="2"/><circle cx="8" cy="4" r="3" fill="#6b449b"/><circle cx="16" cy="4" r="3" fill="#6b449b"/><circle cx="24" cy="4" r="3" fill="#6b449b"/></svg> WOOD</div>
  <div class="search-pair" style="left:523px">FABRIC <svg width="32" height="8"><line x1="2" y1="4" x2="30" y2="4" stroke="#6b449b" stroke-width="2"/><circle cx="8" cy="4" r="3" fill="#6b449b"/><circle cx="16" cy="4" r="3" fill="#6b449b"/><circle cx="24" cy="4" r="3" fill="#6b449b"/></svg> LEATHER</div>
  <div class="search-pair" style="left:766px">METAL <svg width="32" height="8"><line x1="2" y1="4" x2="30" y2="4" stroke="#6b449b" stroke-width="2"/><circle cx="8" cy="4" r="3" fill="#6b449b"/><circle cx="16" cy="4" r="3" fill="#6b449b"/><circle cx="24" cy="4" r="3" fill="#6b449b"/></svg> RUBBER</div>
</section>

<h2 class="abs section-title" style="top:756px">POPULAR PRODUCTS</h2>
<section>
  <article class="abs card product" style="left:124px;top:819px"><div class="product-shot" role="img" aria-label="Glue tube in blister pack"></div><h3>Tackwell Quick Bond Clear Liquid 3ml, (TW-11820)</h3><p>Creates strong bonds for long-lasting results<br>Ultra-fast bonding is quick and convenient<br>Flows into the smallest corners and joints…</p><span class="view-more">View more</span><div class="btn">Buy</div></article>
  <article class="abs card product" style="left:449px;top:819px"><div class="product-shot" role="img" aria-label="Glue tube in blister pack"></div><h3>Tackwell Quick Bond Clear Liquid 3ml, (TW-11820)</h3><p>Creates strong bonds for long-lasting results<br>Ultra-fast bonding is quick and convenient<br>Flows into the smallest corners and joints…</p><span class="view-more">View more</span><div class="btn">Buy</div></article>
  <article class="abs card product" style="left:774px;top:819px"><div class="product-shot" role="img" aria-label="Glue tube in blister pack"></div><h3>Tackwell Quick Bond Clear Liquid 3ml, (TW-11820)</h3><p>Creates strong bonds for long-lasting results<br>Ultra-fast bonding is quick and convenient<br>Flows into the smallest corners and joints…</p><span class="view-more">View more</span><div class="btn">Buy</div></article>
  <article class="abs card product" style="left:124px;top:1248px"><div class="product-shot" role="img" aria-label="Glue tube in blister pack"></div><h3>Tackwell Quick Bond Clear Liquid 3ml, (TW-11820)</h3><p>Creates strong bonds for long-lasting results<br>Ultra-fast bonding is quick and convenient<br>Flows into the smallest corners and joints…</p><span class="view-more">View more</span><div class="btn">Buy</div></article>
  <article class="abs card product" style="left:449px;top:1248px"><div class="product-shot" role="img" aria-label="Glue tube in blister pack"></div><h3>Tackwell Quick Bond Clear Liquid 3ml, (TW-11820)</h3><p>Creates strong bonds for long-lasting results<br>Ultra-fast bonding is quick and convenient<br>Flows into the smallest corners and joints…</p><span class="view-more">View more</span><div class="btn">Buy</div></article>
  <article class="abs card product" style="left:774px;top:1248px"><div class="product-shot" role="img" aria-label="Glue tube in blister pack"></div><h3>Tackwell Quick Bond Clear Liquid 3ml, (TW-11820)</h3><p>Creates strong bonds for long-lasting results<br>Ultra-fast bonding is quick and convenient<br>Flows into the smallest corners and joints…</p><span class="view-more">View more</span><div class="btn">Buy</div></article>
</section>

<section>
  <h2 class="abs faq-title">FAQs</h2>
  <p class="abs faq-sub" style="top:1901px">Can’t find what you’re looking for? Check out some of our most asked questions.</p>
  <div class="abs faq-list">
    <div class="faq-item">Q: What is Lorem Ipsum?</div>
    <div class="faq-item">Q: Why do we use it?</div>
    <div class="faq-item">Q: Where does it come from?</div>
    <div class="faq-item">Q: Where can I get some?</div>
  </div>
  <p class="abs faq-sub" style="top:2273px">Still can’t find what you’re looking for? Ask your question and we’re here to help.</p>
  <div class="abs question-box">Type your question…</div>
  <div class="btn submit">Submit</div>
</section>

<section>
  <h2 class="abs content-title">Content Section</h2>
  <article class="abs card article">
    <div class="article-photo" role="img" aria-label="Close-up of a metal glue tube with clear glue flowing from the nozzle"></div>
    <h2>Heading</h2>
    <p>Lorem ipsum dolor sit amet, consectetur adipiscing elit, sed do eiusmod tempor incididunt ut labore et dolore magna aliqua. Ut enim ad minim veniam, quis nostrud exercitation ullamco laboris nisi ut aliquip ex ea commodo consequat. Duis aute irure dolor in reprehenderit in voluptate velit esse cillum dolore eu fugiat nulla pariatur. Excepteur sint occaecat cupidatat non proident, sunt in culpa qui officia deserunt mollit anim id est laborum.</p>
  </article>
</section>

<section>
  <h2 class="abs blog-title">Blog</h2>
  <article class="abs card post" style="left:124px"><div class="post-photo" role="img" aria-label="Close-up of a gecko foot gripping a surface"></div><h3>Lorem Ipsum Dolor Sit Amet</h3><p>Lorem ipsum dolor sit amet, consectetur adipiscing elit, sed do eiusmod tempor incididunt ut labore et dolore magna aliqua. Ut enim ad minim veniam, quis nostrud exercitation ullamco laboris nisi ut aliquip ex ea</p><div class="btn">Read</div></article>
  <article class="abs card post" style="left:449px"><div class="post-photo" role="img" aria-label="Close-up of a gecko foot gripping a surface"></div><h3>Lorem Ipsum Dolor Sit Amet</h3><p>Lorem ipsum dolor sit amet, consectetur adipiscing elit, sed do eiusmod tempor incididunt ut labore et dolore magna aliqua. Ut enim ad minim veniam, quis nostrud exercitation ullamco laboris nisi ut aliquip ex ea</p><div class="btn">Read</div></article>
  <article class="abs card post" style="left:774px"><div class="post-photo" role="img" aria-label="Close-up of a gecko foot gripping a surface"></div><h3>Lorem Ipsum Dolor Sit Amet</h3><p>Lorem ipsum dolor sit amet, consectetur adipiscing elit, sed do eiusmod tempor incididunt ut labore et dolore magna aliqua. Ut enim ad minim veniam, quis nostrud exercitation ullamco laboris nisi ut aliquip ex ea</p><div class="btn">Read</div></article>
  <div class="btn all-posts">View All Blog Posts</div>
</section>

<footer class="abs footer">
  <div class="footer-brand">CompanyName © 2020</div>
  <div class="footer-links">About<span>|</span>Disclaimers<span>|</span>Contact<span>|</span>Terms &amp; Conditions</div>
</footer>
</body>
</html>
```